Renata Quisby

Luxury And Style -

Black - White & Gold

Target Market(s)

Fashion

Industry/Entity Type

Fashion

Requirements
Must have
• High-End
Nice to have
• We will Print on Silk Paper

```html
<!DOCTYPE html>
<html lang="en">
<head>
<meta charset="utf-8">
<title>Renata Quisby Letterhead</title>
<link href="https://fonts.googleapis.com/css2?family=Poppins:wght@400;500;600&display=swap" rel="stylesheet">
<style>
  :root {
    --paper: #fdfcf9;
    --ink: #141414;
    --ink-soft: #2a2a2a;
    --gold: #b8964a;
    --gold-deep: #9c7a34;
    --black: #0e0e0e;
  }
  * { margin: 0; padding: 0; box-sizing: border-box; }
  html, body { width: 900px; height: 1200px; overflow: hidden; background: var(--paper); }
  .letterhead {
    position: relative; width: 900px; height: 1200px;
    background: var(--paper); color: var(--ink);
    font-family: "Poppins", sans-serif;
  }
  .brand-mark {
    position: absolute; left: 151px; top: 95px; width: 44px; height: 44px;
    border: 1.5px solid var(--gold); border-radius: 50%;
  }
  .brand-name {
    position: absolute; left: 81px; top: 166px;
    font-size: 15px; font-weight: 400; letter-spacing: 5.4px; line-height: 20px;
    color: var(--gold-deep); text-transform: uppercase; white-space: nowrap;
  }
  .letter-date { position: absolute; right: 82px; top: 199px; font-size: 13.5px; color: var(--ink-soft); }
  .letter-date strong { font-weight: 600; color: var(--ink); }
  .sidebar { position: absolute; left: 82px; top: 0; width: 220px; color: var(--ink-soft); }
  .sidebar .block { position: absolute; left: 0; white-space: nowrap; }
  .label-strong { font-size: 16px; font-weight: 600; color: var(--ink); }
  .label { font-size: 13.5px; font-weight: 500; color: var(--ink); }
  .address { font-size: 13px; line-height: 19.5px; }
  .contact-label { font-size: 13px; font-weight: 500; line-height: 16px; color: var(--ink); }
  .contact-value { font-size: 11.5px; line-height: 16px; }
  .divider {
    position: absolute; left: 311px; top: 292px; width: 1.5px; height: 636px;
    background: var(--gold);
  }
  .salutation { position: absolute; top: 288px; left: 372px; font-size: 22px; font-weight: 600; color: var(--ink); }
  .letter-body { position: absolute; left: 372px; width: 446px; color: var(--ink-soft); }
  .letter-body p { font-size: 11.2px; line-height: 18.5px; }
  .letter-body .line { display: block; white-space: nowrap; text-align: justify; text-align-last: justify; }
  .letter-body .line.end { text-align-last: left; }
  .sign-name { position: absolute; left: 372px; top: 805px; font-size: 21px; font-weight: 600; color: var(--ink); }
  .sign-role { position: absolute; left: 373px; top: 837px; font-size: 12.5px; color: var(--ink-soft); }
  .signature-area {
    position: absolute; left: 372px; top: 866px; width: 196px; height: 62px;
    background: linear-gradient(90deg, rgba(20,20,20,.14), rgba(20,20,20,.04));
    border-radius: 4px;
  }
  .footer-band { position: absolute; left: 0; bottom: 0; width: 900px; height: 85px; }
</style>
</head>
<body>
<main class="letterhead">
  <span class="brand-mark"></span>
  <div class="brand-name">Renata Quisby</div>

  <div class="letter-date"><strong>Date:</strong> Octobor 06th, 2025</div>

  <aside class="sidebar">
    <div class="block" style="top:287px"><div class="label-strong">To</div></div>
    <div class="block address" style="top:323px">123 Anywhere Address.,<br>Any City, Location Here</div>
    <div class="block" style="top:403px"><div class="label">Your Name</div></div>
    <div class="block address" style="top:430px">123 Anywhere Address.,<br>Any City, 2nd Location Here</div>
    <div class="block" style="top:549px"><div class="contact-label">Phone</div><div class="contact-value">+1234 56789</div></div>
    <div class="block" style="top:592px"><div class="contact-label">Email</div><div class="contact-value">www.youremailhere</div></div>
    <div class="block" style="top:638px"><div class="contact-label">Website</div><div class="contact-value">www.yourwebsite.com</div></div>
    <div class="block" style="top:685px"><div class="contact-label">Address</div><div class="contact-value">www.your address here</div></div>
  </aside>

  <div class="divider"></div>

  <h1 class="salutation">Dear Sir/Madam</h1>
  <div class="letter-body" style="top:342px">
    <p>
      <span class="line">Lorem ipsum dolor sit amet, consectetuer adipiscing elit, sed diam</span>
      <span class="line">nonummy nibh euismod tincidunt ut laoreet dolore magna aliquam erat</span>
      <span class="line">volutpat. Ut wisi enim ad minim veniam, quis nostrud exerci tation</span>
      <span class="line">ullamcorper suscipit lobortis nisl ut aliquip ex ea commodo consequat.</span>
      <span class="line">Duis autem vel eum iriure dolor in hendrerit in vulputate velit esse molestie</span>
      <span class="line">consequat, vel illum dolore eu feugiat nulla facilisis at vero eros et</span>
      <span class="line">accumsan et iusto odio dignissim qui blandit praesent luptatum zzril</span>
      <span class="line end">delenit augue duis dolore te feugait nulla facilisi.</span>
    </p>
  </div>
  <div class="letter-body" style="top:523px">
    <p>
      <span class="line">Lorem ipsum dolor sit amet, consectetuer adipiscing elit, sed diam</span>
      <span class="line">nonummy nibh euismod tincidunt ut laoreet dolore magna aliquam erat</span>
      <span class="line">volutpat. Ut wisi enim ad minim veniam, quis nostrud exerci tation</span>
      <span class="line">ullamcorper suscipit lobortis nisl ut aliquip ex ea commodo consequat.</span>
      <span class="line">Duis autem vel eum iriure dolor in hendrerit in vulputate velit esse molestie</span>
      <span class="line end">consequat,</span>
    </p>
  </div>
  <div class="letter-body" style="top:667px">
    <p>
      <span class="line">Lorem ipsum dolor sit amet, consectetuer adipiscing elit, sed diam</span>
      <span class="line">nonummy nibh euismod tincidunt ut laoreet dolore magna aliquam erat</span>
      <span class="line end">volutpat.</span>
    </p>
  </div>

  <div class="sign-name">Edwin Falloway</div>
  <div class="sign-role">Manager</div>
  <div class="signature-area" role="img" aria-label="Handwritten signature"></div>

  <svg class="footer-band" viewBox="0 0 900 85" aria-hidden="true">
    <path d="M0 30 H359 C400 30 410 68 450 68 C490 68 500 30 546 30 H900 V85 H0 Z" fill="var(--black)"/>
    <path d="M0 30 H359 C400 30 410 68 450 68 C490 68 500 30 546 30 H900" fill="none" stroke="var(--gold)" stroke-width="1.5"/>
    <circle cx="450" cy="27" r="27" fill="none" stroke="var(--gold)" stroke-width="1.2"/>
  </svg>
</main>
</body>
</html>
```